Corwyns Best 4 years in a row

I need a billboard that has all the attached logos and says:

Corwyn's Best Realtor 4 Years in a row!

1.75 Listing Fee

Tobias Wrenfield

555-214-7390

and somewhere very small at the bottom:

855-555-0142

2748 W Amberlow Rd, Fernhollow, NC 20957

I put in the last winner just to give an idea of what I'm looking for, although I'd like to switch it up a little bit.

```html
<!DOCTYPE html>
<html lang="en">
<head>
<meta charset="utf-8">
<title>Tobias Wrenfield – Billboard</title>
<link href="https://fonts.googleapis.com/css2?family=Barlow:wght@400;500&display=swap" rel="stylesheet">
<style>
  :root {
    --navy: #1b2f5e;
    --band-grey: #a2a2a2;
    --fee-grey: #9c9c9c;
    --white: #ffffff;
    --ink: #111111;
    --badge: #1e1e1e;
    --page: #f2f2f2;
    --photo-light: #e9e6e3;
    --photo-dark: #2e3648;
  }
  html, body {
    margin: 0;
    width: 1200px;
    height: 1200px;
    overflow: hidden;
    background: var(--page);
  }
  .billboard {
    position: absolute;
    left: 40px;
    top: 432px;
    width: 1120px;
    height: 336px;
    background: var(--white);
    overflow: hidden;
    font-family: "Barlow", sans-serif;
  }
  .billboard__shapes {
    position: absolute;
    inset: 0;
  }
  .agent-name, .agent-phone, .listing-fee, .contact-line, .headline, .team-name {
    position: absolute;
    margin: 0;
    white-space: nowrap;
  }
  .agent-name {
    left: 58px;
    top: 38px;
    font-size: 47px;
    line-height: 56px;
    font-weight: 400;
    color: var(--white);
  }
  .agent-phone {
    left: 58px;
    top: 94px;
    font-size: 53px;
    line-height: 62px;
    font-weight: 500;
    color: var(--white);
  }
  .listing-fee {
    left: 58px;
    top: 209px;
    font-size: 35px;
    line-height: 42px;
    font-weight: 400;
    color: var(--white);
  }
  .contact-line {
    left: 58px;
    top: 282px;
    font-size: 15px;
    line-height: 20px;
    color: var(--ink);
  }
  .headline {
    right: 48px;
    top: 32px;
    text-align: right;
    font-size: 40px;
    font-weight: 400;
    line-height: 49px;
    color: var(--white);
  }
  .agent-photo {
    position: absolute;
    left: 470px;
    top: 24px;
    width: 220px;
    height: 312px;
    background: linear-gradient(180deg, var(--photo-light) 0%, var(--photo-dark) 45%, var(--photo-dark) 100%);
    border-radius: 90px 90px 0 0;
  }
  .team-name {
    left: 756px;
    top: 215px;
    width: 160px;
    text-align: center;
    font-size: 19px;
    font-weight: 500;
    line-height: 24px;
    color: var(--navy);
  }
  .award-badge {
    position: absolute;
    left: 938px;
    top: 181px;
    width: 130px;
    height: 130px;
    border-radius: 50%;
    background: var(--badge);
  }
</style>
</head>
<body>
  <section class="billboard">
    <svg class="billboard__shapes" width="1120" height="336" viewBox="0 0 1120 336">
      <polygon class="name-panel" points="0,0 553,0 600,188 0,188" fill="var(--navy)"/>
      <polygon class="headline-band" points="553,0 1120,0 1120,156 592,156" fill="var(--band-grey)"/>
      <rect class="fee-band" x="0" y="201" width="532" height="58" fill="var(--fee-grey)"/>
    </svg>

    <h1 class="agent-name">Tobias Wrenfield</h1>
    <p class="agent-phone">555-214-7390</p>
    <p class="listing-fee">1.75 Listing Fee</p>
    <p class="contact-line">855-555-0142 | 2748 W Amberlow Rd, Fernhollow, NC 20957</p>

    <div class="agent-photo" role="img" aria-label="Portrait photo of the realtor in a navy suit"></div>

    <h2 class="headline">Corwyn's Best Realtor<br>4 Years in a row!</h2>

    <p class="team-name">The Summit Team<br>Keystone Realty</p>
    <div class="award-badge" role="img" aria-label="Award badge"></div>
  </section>
</body>
</html>
```